Existing Logo Post Card Design for Residential and Commercial Services Company

We are looking for a Post card design for bulk mail along with letterhead and business cards for a new Residential and Commercial Services company. We focus on senior citizens and vets with the idea of "One Call Every Service". We provide landscaping, pressure washing, maid service, and pest control to both the commercial and residential market. We also provide estimates, proposal creation, scheduling, cost controls and consulting to contractors.
The mailer is going to be targeting the residential services portion of the business and heading out to advertise our landscaping, pressure washing and maid services. It should use the primary color of red, white and blue. If the logo need to be tweaked on shades, please feel free to do that. More than just service we sell security to our customers because we are not the average residential services company.
The sample business card designs that have been uploaded are from another company that we currently own and we like the cards. We would like to keep it simple on the back of the card with the colors and the company slogan of “One Call Every Service”.
We also like the layout of the front of the card with the logo boldly displayed. The company name should also be display on the card “Taldrim Works” Please make sure there is a name, address, phone number, email address and website www.taldrimworks.example on the front of the card as well.
We would like the letter head to display the logo in the top left of the page with space for phone number, address, and website at the bottom of the page. We would like the info at the bottom of the page to be in a straight line across the bottom of the page. The page dimensions should be 8.5X11” and there should be a .5” margin around the complete perimeter of the page.
Thanks and good luck

Target Market(s)

Homeowners with a focus on Senior citizens and Vets

Industry/Entity Type

Residential Construction

Contact Information for Business Card

The business card should focus on Red, white and blue it will be 2 sided and should be bold and will be foiled.

Font styles to use
Serif

Requirements
Must have
• The Company slogan should be displayed on the back side of the card "One Call Every Service" it should also be easy to read
Nice to have
• The card should be Red, White, Blue and primarily black text.
Should not have
• Please refrain hard to read text it should be clear and easy to read

```html
<!DOCTYPE html>
<html lang="en">
<head>
<meta charset="utf-8">
<title>Taldrim Works Mailer</title>
<link href="https://fonts.googleapis.com/css2?family=Bebas+Neue&family=Raleway:wght@800&display=swap" rel="stylesheet">
<style>
  :root {
    --brand-red: #c1202f;
    --brand-blue: #1f3f9a;
    --white: #ffffff;
    --room-light: #f4f5f6;
    --room-mid: #e3e5e8;
  }
  html, body {
    margin: 0;
    padding: 0;
    width: 1200px;
    height: 930px;
    overflow: hidden;
    background: var(--white);
  }
  .mailer {
    position: absolute;
    left: 0;
    top: 0;
    width: 580px;
    height: 766px;
    overflow: hidden;
  }
  .hero-photo {
    position: absolute;
    left: 0;
    top: 0;
    width: 580px;
    height: 630px;
    background:
      radial-gradient(ellipse at 20% 15%, #ffffff 0%, rgba(255,255,255,0) 60%),
      linear-gradient(180deg, var(--room-light) 0%, #eceef0 55%, var(--room-mid) 100%);
  }
  .brand-name {
    position: absolute;
    left: 190px;
    top: 36px;
    margin: 0;
    font-family: 'Bebas Neue', sans-serif;
    font-weight: 400;
    font-size: 76px;
    line-height: 1;
    color: var(--brand-red);
    letter-spacing: 0.5px;
    white-space: nowrap;
  }
  .service-list {
    position: absolute;
    left: 193px;
    top: 162px;
    margin: 0;
    padding: 0;
    list-style: none;
    font-family: 'Bebas Neue', sans-serif;
    font-size: 39px;
    line-height: 43.6px;
    color: var(--brand-red);
    white-space: nowrap;
    transform: scaleX(0.94);
    transform-origin: left top;
  }
  .service-list li::before {
    content: "";
    display: inline-block;
    width: 9px;
    height: 9px;
    border-radius: 50%;
    background: var(--brand-red);
    margin-right: 6px;
    vertical-align: 8px;
  }
  .slogan {
    position: absolute;
    left: 202px;
    top: 482px;
    margin: 0;
    font-family: 'Bebas Neue', sans-serif;
    font-weight: 400;
    font-size: 90px;
    line-height: 70px;
    white-space: nowrap;
    transform: scaleX(0.86);
    transform-origin: left top;
  }
  .slogan-top { display: block; color: var(--brand-red); }
  .slogan-bottom { display: block; color: var(--brand-blue); }
  .trust-band {
    position: absolute;
    left: 0;
    top: 630px;
    width: 580px;
    height: 136px;
    background: var(--brand-red);
    display: flex;
    align-items: center;
    justify-content: center;
  }
  .trust-band p {
    margin: 0;
    font-family: 'Raleway', sans-serif;
    font-weight: 800;
    font-size: 26px;
    line-height: 33px;
    color: var(--white);
    text-align: center;
    text-transform: uppercase;
  }
</style>
</head>
<body>
  <section class="mailer">
    <div class="hero-photo" role="img" aria-label="Bright white living room with a sofa, rug and a red cleaning bucket with mop and supplies"></div>
    <h1 class="brand-name">Taldrim Works</h1>
    <ul class="service-list">
      <li>Lawn Maintenance</li>
      <li>Landscaping</li>
      <li>Roof Cleaning</li>
      <li>House Washing</li>
      <li>Fence and Deck Restoration</li>
      <li>Maid Service</li>
      <li>Handyman Service</li>
    </ul>
    <h2 class="slogan">
      <span class="slogan-top">One Call</span>
      <span class="slogan-bottom">Every Service</span>
    </h2>
    <div class="trust-band">
      <p>All employees are background<br>checked and drug tested for your<br>safety and security</p>
    </div>
  </section>
</body>
</html>
```